Revamping and duplicating of existing business card

We are a painting and decorating business based in London and need a couple of business cards made up for the following people.

1. Marla Penhallow
2. Toby Renwick

Measurements - 85 X 55 mm
Font: Blue highway
Colour: No idea! Would be great to have a pantone for the pink if possible?

I’ve attached all the logos and old artwork etc.
Here are the amendments I would definitely like...

1. Marla

format mobile number correctly: 07451 386 902

Add title: Decorator
Use: Penhallow Decorating Logo
Add twitter logo & @penhallowdecor
Add tradeverify logo
Add HFG Logo
Make it all look beautiful/revamp/tweak - whatever you think…

2. Toby

Decorator

07623 519 840
toby@penhallowdecorating.co.uk
Updates

Hello! Thanks so much for all your designs. This is such a great way to get these things done... Just to clarify, Please do not alter our logo at all. The 'splat' appears on our van, tshirts, quotes etc and is very much part of our branding. Colour scheme: Pink, black and white. Thanks Marla

Reason: Not 100% sold on any of the designs so far but very grateful for all the submissions. Keep it simple and quirky please. Thanks Marla

Industry/Entity Type

Painting

Requirements
Must have
• Pink & Black Colour scheme
Penhallow Decorating Logo
Blue Highway font

```html
<!DOCTYPE html>
<html lang="en">
<head>
<meta charset="utf-8">
<title>Penhallow Decorating – Business Cards</title>
<link rel="stylesheet" href="https://fonts.googleapis.com/css2?family=Ubuntu:wght@400;500;700&display=swap">
<style>
  :root {
    --pink-deep: #d81b6a;
    --pink-bright: #e3237f;
    --pink-soft: #f0a6c6;
    --pink-pale: #f8d3e2;
    --white: #ffffff;
    --ink: #1d1d1b;
    --badge-blue: #2a5ea8;
    --icon-blue: #5fb4e0;
    --verify-red: #d8232a;
  }
  * { margin: 0; padding: 0; box-sizing: border-box; }
  html, body { width: 1000px; height: 1200px; overflow: hidden; background: var(--white); }
  body { position: relative; font-family: "Ubuntu", sans-serif; color: var(--ink); }

  .card {
    position: absolute;
    left: 220px;
    width: 516px;
    height: 334px;
    overflow: hidden;
    box-shadow: 0 4px 14px rgba(0,0,0,0.35);
  }
  .card--marla { top: 56px; }
  .card--back { top: 435px; }
  .card--toby { top: 814px; }

  .splat-art {
    position: absolute; inset: 0;
    background: linear-gradient(135deg,
      var(--pink-deep) 0%, var(--pink-deep) 38%,
      var(--pink-soft) 58%, var(--pink-pale) 70%, var(--white) 82%);
  }
  .splat-art--back {
    background: radial-gradient(circle at 30% 35%, var(--pink-deep) 0%, var(--pink-deep) 45%, var(--pink-bright) 100%);
  }

  .brand {
    position: absolute; left: 33px; top: 40px;
    font-weight: 500; color: var(--ink); line-height: 1;
  }
  .brand__name { display: block; font-size: 50px; letter-spacing: -0.5px; }
  .brand__trade { display: block; font-size: 36px; margin-top: 4px; }

  .person {
    position: absolute; right: 28px; top: 36px; text-align: right; line-height: 1.05;
  }
  .person__name { font-size: 15px; font-weight: 700; }
  .person__role { font-size: 11px; font-weight: 700; }

  .contact {
    position: absolute; right: 28px; top: 202px; text-align: right;
    font-size: 16px; font-weight: 500; line-height: 22px;
  }
  .contact__social {
    display: flex; justify-content: flex-end; align-items: center; gap: 8px;
    margin-top: 4px; color: var(--pink-deep);
  }
  .contact__social-icon {
    width: 26px; height: 26px; border-radius: 3px; background: var(--icon-blue);
  }

  .memberships {
    position: absolute; right: 28px; bottom: 14px;
    display: flex; align-items: center; gap: 14px;
  }
  .memberships__listing { line-height: 1; }
  .memberships__lead { font-size: 6px; display: block; margin-bottom: 2px; }
  .memberships__name { font-size: 17px; font-weight: 700; color: var(--verify-red); }
  .memberships__badge {
    width: 34px; height: 34px; border-radius: 50%;
    background: var(--white); border: 3px solid var(--badge-blue);
  }

  .web-address {
    position: absolute; left: 0; right: 0; top: 162px; text-align: center;
    font-size: 22px; font-weight: 500; letter-spacing: 2.4px; color: var(--ink);
  }
</style>
</head>
<body>

<section class="card card--marla">
  <div class="splat-art" role="img" aria-label="Pink and white paint splat artwork"></div>
  <h1 class="brand"><span class="brand__name">Penhallow</span><span class="brand__trade">Decorating</span></h1>
  <div class="person">
    <p class="person__name">Marla Penhallow</p>
    <p class="person__role">Decorator</p>
  </div>
  <div class="contact">
    <p>Tel: 07451 386 902</p>
    <p>marla@penhallowdecorating.co.uk</p>
    <p class="contact__social"><span class="contact__social-icon"></span>@penhallowdecor</p>
  </div>
  <div class="memberships">
    <p class="memberships__listing"><span class="memberships__lead">Proud members of</span><span class="memberships__name">tradeverify</span></p>
    <span class="memberships__badge" role="img" aria-label="HFG membership badge"></span>
  </div>
</section>

<section class="card card--back">
  <div class="splat-art splat-art--back" role="img" aria-label="Tonal pink paint splat artwork"></div>
  <p class="web-address">www.penhallowdecorating.co.uk</p>
</section>

<section class="card card--toby">
  <div class="splat-art" role="img" aria-label="Pink and white paint splat artwork"></div>
  <h1 class="brand"><span class="brand__name">Penhallow</span><span class="brand__trade">Decorating</span></h1>
  <div class="person">
    <p class="person__name">Toby Renwick</p>
    <p class="person__role">Decorator</p>
  </div>
  <div class="contact">
    <p>Tel: 07623 519 840</p>
    <p>toby@penhallowdecorating.co.uk</p>
    <p class="contact__social"><span class="contact__social-icon"></span>@penhallowdecor</p>
  </div>
  <div class="memberships">
    <p class="memberships__listing"><span class="memberships__lead">Proud members of</span><span class="memberships__name">tradeverify</span></p>
    <span class="memberships__badge" role="img" aria-label="HFG membership badge"></span>
  </div>
</section>

</body>
</html>
```